Vasel Tea Label & packaging for a premium tea brand. For local and global market

Create a look and feel for a box and rectangle tin. We are looking for a luxe packaging design for a new tea brand based in Kenya called 'Vasel Tea'. Kenya is home to the finest teas in the world and Vasel tea looks to embody that fact. Vasel Tea uses the most premium of Kenyan Tea, Black tea, Purple tea, White Tea, Green tea, Hibiscus Tea and Moringa Tea. Vasel Tea is handpicked from Kenya's highlands. This project will include the look and feel of the different teas described above. The copy on the main face of the box should read 'Premium Kenyan Tea' The box will contain 25 tagged tea bags, with a net weight of 50 gms.

On one side of the box will read 'packaging instructions' To fully savour this Vasel premium tea, use one tea bag for each cup, add some freshly bolded water and wait for 2 minutes as you enjoy the sweet aroma of our tea, stir and serve' Ingredients : Black Tea, and for the others the same : Hibiscus Tea, Green Tea, Purple Tea, White tea. should also feature on the label: Produce of Kenya.

Target Market(s)

Premium

Industry/Entity Type

Agribusiness

Font styles to use
Script

Colors

Designer to choose colors to be used in the design.

Requirements
Must have
• Luxe look and feel
Nice to have
• I have attached the Vasel tea logo and images of brands I'd lile the designer to be inspired by.
Should not have
• Green and yellow colours

```html
<!DOCTYPE html>
<html lang="en">
<head>
<meta charset="utf-8">
<title>Vasel Tea – Hibiscus Tea Label</title>
<link rel="stylesheet" href="https://fonts.googleapis.com/css2?family=Great+Vibes&family=Josefin+Sans:wght@300&family=Libre+Baskerville&display=swap">
<style>
  :root {
    --page: #ffffff;
    --label: #1d1d1e;
    --label-edge: #262627;
    --ink: #f2f2f2;
    --ink-soft: #c9c9c9;
    --accent: #e45a6c;
    --petal: #e0233a;
    --petal-deep: #a8132a;
    --petal-light: #f1566a;
    --wine: #5a1522;
  }
  * { box-sizing: border-box; margin: 0; padding: 0; }
  html, body {
    width: 1200px;
    height: 880px;
    overflow: hidden;
    background: var(--page);
  }
  .canvas {
    position: relative;
    width: 1200px;
    height: 880px;
  }
  .tin-label {
    position: absolute;
    left: 425px;
    top: 200px;
    width: 350px;
    height: 480px;
    background: linear-gradient(180deg, var(--label-edge) 0%, var(--label) 40%);
    overflow: hidden;
  }
  .label-line {
    position: absolute;
    left: 0;
    width: 100%;
    text-align: center;
    white-space: nowrap;
  }
  .brand-name {
    top: 78px;
    font-family: "Josefin Sans", sans-serif;
    font-weight: 300;
    font-size: 56px;
    letter-spacing: 3px;
    line-height: 1;
    color: var(--ink);
  }
  .product-name {
    top: 144px;
    font-family: "Libre Baskerville", serif;
    font-size: 15px;
    letter-spacing: 1.5px;
    line-height: 1;
    color: var(--ink);
  }
  .tagline {
    top: 164px;
    font-family: "Great Vibes", cursive;
    font-size: 24px;
    line-height: 1.2;
    color: var(--accent);
  }
  .pack-contents {
    top: 200px;
    font-family: "Josefin Sans", sans-serif;
    font-weight: 300;
    font-size: 11px;
    letter-spacing: 1.2px;
    line-height: 1;
    color: var(--ink-soft);
  }
  .hibiscus-illustration {
    position: absolute;
    left: 0;
    top: 222px;
    width: 350px;
    height: 222px;
    background:
      radial-gradient(ellipse 110px 100px at 145px 120px, var(--petal-light) 0%, var(--petal) 45%, var(--petal-deep) 80%, transparent 100%),
      radial-gradient(ellipse 90px 80px at 290px 100px, var(--wine) 0%, transparent 100%),
      radial-gradient(ellipse 60px 90px at 20px 110px, var(--wine) 0%, transparent 100%);
  }
  .origin {
    top: 454px;
    font-family: "Josefin Sans", sans-serif;
    font-weight: 300;
    font-size: 10px;
    letter-spacing: 2px;
    line-height: 1;
    color: var(--ink-soft);
  }
</style>
</head>
<body>
  <main class="canvas">
    <section class="tin-label">
      <h1 class="label-line brand-name">VASEL</h1>
      <p class="label-line product-name">HIBISCUS TEA</p>
      <p class="label-line tagline">Premium Kenyan Tea</p>
      <p class="label-line pack-contents">25 BAGS . 50g</p>
      <div class="hibiscus-illustration" role="img" aria-label="Botanical illustration of a red hibiscus flower with long stamen and leaves"></div>
      <p class="label-line origin">PRODUCE OF KENYA</p>
    </section>
  </main>
</body>
</html>
```